Flyer Design Project

Need a DL Size flyer (2 sided) for letter box marketing for our website www.brightwardsecure.com.au

Project Deadline Extended
Reason: Thank you for submitting the designs. We like few of the designs and will request those designers to changes few things to make it more suitable for us. Because of holidays need to extend the deadlines. Thank you.

Industry/Entity Type

Marketing

```html
<!DOCTYPE html>
<html lang="en">
<head>
<meta charset="utf-8">
<title>Brightward Secure – DL Flyer</title>
<link href="https://fonts.googleapis.com/css2?family=Arimo:wght@400;700&family=Questrial&display=swap" rel="stylesheet">
<style>
  :root{
    --page:#e9ecef;
    --blue-deep:#0b4f9c;
    --blue-mid:#1f7fd1;
    --blue-sky:#7cc4f0;
    --blue-pale:#e6f4fd;
    --yellow:#f7c81e;
    --navy:#0f2c5a;
    --ink:#1a1a1a;
    --pill:#1c6fc4;
    --dash:#f0a53a;
    --white:#ffffff;
  }
  *{box-sizing:border-box;margin:0;padding:0}
  html,body{width:1174px;height:1200px;overflow:hidden}
  body{background:var(--page);font-family:"Arimo",Arial,sans-serif;position:relative;color:var(--ink)}

  .flyer{position:absolute;left:102px;width:970px;height:456px;overflow:hidden;box-shadow:0 6px 16px rgba(0,0,0,.18)}
  .flyer--front{top:90px;background:var(--blue-pale)}
  .flyer--back{top:630px;background:var(--white)}

  /* front */
  .header{position:absolute;left:0;top:0;width:100%;height:94px;
    background:linear-gradient(90deg,var(--blue-deep) 0%,var(--blue-mid) 40%,var(--blue-sky) 100%)}
  .brand{position:absolute;left:30px;top:18px;display:flex;align-items:center;gap:14px}
  .brand__mark{width:54px;height:54px;background:var(--white);border-radius:4px}
  .brand__name{font-family:"Arimo",sans-serif;font-weight:700;font-size:33px;color:var(--yellow);line-height:1}
  .brand__tag{font-weight:700;font-size:17px;color:var(--white);margin-top:5px}
  .header__call{position:absolute;right:30px;top:30px;font-family:"Questrial",sans-serif;font-size:30px;color:var(--yellow)}

  .backdrop{position:absolute;left:0;top:94px;width:100%;height:362px;
    background:linear-gradient(165deg,#f3f9fe 0%,#cfe8f9 35%,#5ea9e4 62%,#8ccaf2 100%)}

  .photo{position:absolute;border-radius:6px}
  .photo--dome{left:80px;top:143px;width:127px;height:143px;
    background:linear-gradient(180deg,#f1f2f4 0%,#c9cdd2 60%,#7d838b 100%)}
  .photo--phones{left:300px;top:115px;width:262px;height:200px;
    background:linear-gradient(90deg,#2b2d31 0%,#7a6a5a 30%,#4a8fb4 60%,#2e2f33 100%)}
  .photo--monitor{left:645px;top:115px;width:257px;height:204px;
    background:linear-gradient(180deg,#8c8f93 0%,#b8a078 55%,#2a2b2e 90%)}

  .pill{position:absolute;height:26px;border-radius:13px;background:var(--pill);
    color:var(--white);font-family:"Questrial",sans-serif;font-size:12.5px;display:flex;align-items:center;justify-content:center}
  .pill--a{left:44px;top:306px;width:196px}
  .pill--b{left:342px;top:330px;width:196px}
  .pill--c{left:632px;top:330px;width:278px}

  .about{position:absolute;left:36px;top:348px;width:262px}
  .about__title{font-family:"Questrial",sans-serif;font-size:21px;color:var(--ink);margin-bottom:4px}
  .about__text{font-family:"Questrial",sans-serif;font-size:12px;line-height:1.22;text-align:justify}
  .site{position:absolute;right:30px;top:390px;font-family:"Questrial",sans-serif;font-size:33px;color:var(--white)}

  /* back */
  .packages__title{position:absolute;left:30px;top:14px;font-weight:700;font-size:23px;color:var(--blue-mid)}
  .packages__intro{position:absolute;left:30px;top:43px;font-size:10.5px;color:#333}
  .pkg{position:absolute;width:463px;height:89px;border:1.5px dashed var(--dash);border-radius:12px;padding:5px 14px}
  .pkg--l{left:14px}.pkg--r{left:486px}
  .pkg--1,.pkg--4{top:61px}.pkg--2,.pkg--5{top:158px}.pkg--3,.pkg--6{top:254px}
  .pkg__name{font-weight:700;font-size:19px;color:var(--blue-mid);margin-bottom:2px}
  .pkg__spec{font-size:10.5px;line-height:1.28;list-style:none;color:#222}
  .pkg__photo{position:absolute;right:18px;top:10px;width:150px;height:68px;border-radius:4px;
    background:linear-gradient(90deg,#3a3d42 0%,#c8ccd1 55%,#f1f2f3 100%)}
  .common{position:absolute;left:30px;top:352px;font-weight:700;font-size:13px;color:var(--blue-mid)}

  .band{position:absolute;left:0;top:374px;width:100%;height:82px;
    background:linear-gradient(90deg,var(--blue-deep) 0%,var(--blue-mid) 45%,var(--blue-sky) 100%)}
  .band__list{position:absolute;left:28px;top:6px;list-style:none;color:var(--white);font-size:11px;line-height:1.3}
  .band__contact{position:absolute;left:470px;top:20px;font-weight:700;font-size:26px;color:var(--yellow)}
  .band__rule{position:absolute;left:628px;top:10px;width:1.5px;height:62px;background:var(--yellow)}
  .band__details{position:absolute;left:640px;top:8px;color:var(--navy);line-height:1.15}
  .band__addr{font-size:13px}
  .band__phone,.band__web{font-size:18px}
</style>
</head>
<body>

<section class="flyer flyer--front">
  <div class="backdrop" role="img" aria-label="Flowing blue wave background"></div>

  <header class="header">
    <div class="brand">
      <div class="brand__mark"></div>
      <div>
        <div class="brand__name">Brightward Secure</div>
        <div class="brand__tag">CCTV System Specialist</div>
      </div>
    </div>
    <div class="header__call">Call Us: 02 5550 1847</div>
  </header>

  <div class="photo photo--dome" role="img" aria-label="Dome security camera"></div>
  <div class="photo photo--phones" role="img" aria-label="Three smartphones showing live camera views"></div>
  <div class="photo photo--monitor" role="img" aria-label="LCD monitor showing multi-camera recording grid"></div>

  <div class="pill pill--a">High Rwsolution cctv system</div>
  <div class="pill pill--b">Remote access Smart phone</div>
  <div class="pill pill--c">Motion detection camera or 24/7 Recordings</div>

  <div class="about">
    <h2 class="about__title">About Us</h2>
    <p class="about__text">Brightward Secure is dedicated to providing high quality CCTV System at affordable prices. All of our packages include hardware, software, accessories and full installation.</p>
  </div>
  <div class="site">www.brightwardsecure.com.au</div>
</section>

<section class="flyer flyer--back">
  <h2 class="packages__title">Customized Packages</h2>
  <p class="packages__intro">We offer a variety of CCTV system packages that are reliable, affordable and easy to use. Below are some of the packages that are suitable for a home or small business.</p>

  <article class="pkg pkg--l pkg--1">
    <h3 class="pkg__name">Package 1</h3>
    <ul class="pkg__spec"><li>Standalone DVR System (2 Cameras)</li><li>2 X high resolution dome cameras</li><li>1 X 2 channel standalone DVR</li><li>500GB hard drive</li></ul>
    <div class="pkg__photo" role="img" aria-label="Monitor, DVR and two dome cameras"></div>
  </article>
  <article class="pkg pkg--l pkg--2">
    <h3 class="pkg__name">Package 2</h3>
    <ul class="pkg__spec"><li>Standalone DVR System (4 Cameras)</li><li>4 X high resolution dome cameras</li><li>1 X 4 channel standalone DVR</li><li>500GB hard drive</li></ul>
    <div class="pkg__photo" role="img" aria-label="Monitor, DVR and four dome cameras"></div>
  </article>
  <article class="pkg pkg--l pkg--3">
    <h3 class="pkg__name">Package 3</h3>
    <ul class="pkg__spec"><li>Standalone DVR System (8 Cameras)</li><li>8 X high resolution dome cameras</li><li>1 X 8 channel standalone DVR</li><li>1 Terrabyte hard drive</li></ul>
    <div class="pkg__photo" role="img" aria-label="Monitor, DVR and eight dome cameras"></div>
  </article>
  <article class="pkg pkg--r pkg--4">
    <h3 class="pkg__name">Package 4</h3>
    <ul class="pkg__spec"><li>IP based CCTV System (2 Cameras)</li><li>2 X 2 Megapixel IP Cameras</li><li>1 X PC based NVR System</li><li>500GB hard drive</li></ul>
    <div class="pkg__photo" role="img" aria-label="PC with monitor and two IP cameras"></div>
  </article>
  <article class="pkg pkg--r pkg--5">
    <h3 class="pkg__name">Package 5</h3>
    <ul class="pkg__spec"><li>IP based CCTV System (4 Cameras)</li><li>4 X 2 Megapixel IP Cameras</li><li>1 X PC based NVR System</li><li>1 Terrabyte hard drive</li></ul>
    <div class="pkg__photo" role="img" aria-label="PC with monitor and four IP cameras"></div>
  </article>
  <article class="pkg pkg--r pkg--6">
    <h3 class="pkg__name">Package 6</h3>
    <ul class="pkg__spec"><li>IP based CCTV System (8 Cameras)</li><li>8 X 2 Megapixel IP Cameras</li><li>1 X PC based NVR System</li><li>2 Terrabyte hard drive</li></ul>
    <div class="pkg__photo" role="img" aria-label="PC with monitor and eight IP cameras"></div>
  </article>

  <p class="common">Common Specfication For All The Packages Are</p>

  <footer class="band">
    <ul class="band__list">
      <li>19" LCD monitor</li><li>Remote access from PCs &amp; Phones*</li><li>Easy to use</li><li>1 Year Warranty</li><li>Full system supplied &amp; installed</li>
    </ul>
    <div class="band__contact">Contact us</div>
    <div class="band__rule"></div>
    <div class="band__details">
      <div class="band__addr">14/6 Marlow Street, Kelvin Grove, NSW 2199</div>
      <div class="band__phone">Call Us: 02 5550 1847</div>
      <div class="band__web">www.brightwardsecure.com.au</div>
    </div>
  </footer>
</section>

</body>
</html>
```